Merelunda layout redesign brief

Merelunda.example is a functional site developed in Ruby on Rails for which we wish to overhaul the layout and overall design concepts. New page designs must incorporate the existing functionality and work flows and allow the user interactions already defined.

Redesign of the primary logo is not included in the brief.

The objective of Merelunda is to provide an holistic approach to developing a healthy lifestyle including diet, exercise and mental well-being by providing a series of tools and interactions. All three elements must be included

The designer must demonstrate that they have utilised the site in order to gain an understanding of the various component available. MereLunda needs multiple levels of engagement, needs to be responsive, along the lines to allow the users to anticipate the opportunity of becoming a member. We need to be able to display synopsis of members blogs, successes and other news items as we see fit on the landing page.

Target Market(s)

Aimed at 18-65 male and female with an interest in changing their lifestyle to be healthier, fitter and a stronger confidence in their self-image. This site is about taking personal responsibility of your own life using the emotional support available through the tools and interactions within the site.

Requirements
Must have
• Must have the merelunda logo.
Must retain the sections (though not necessarily the names of the sections)
Make use of colours, graphics and images.
Appropriate use of popup overlays for providing help and support.
Community features
Space for advertisers

```html
<!DOCTYPE html>
<html lang="en">
<head>
<meta charset="utf-8">
<title>MereLunda – Be Fitter, Be Healthier, Be In Control</title>
<link href="https://fonts.googleapis.com/css2?family=Lato:wght@300;400;700;900&family=Kaushan+Script&display=swap" rel="stylesheet">
<style>
  :root{
    --brand-green:#7fc31c;
    --tab-green:#8ccb23;
    --hero-top:#e6f1d2;
    --hero-bottom:#d7ecbf;
    --accent-yellow:#f5cf3c;
    --action-blue:#0a8fd6;
    --page-grey:#f4f4f4;
    --card-white:#ffffff;
    --ink-dark:#222222;
    --ink-mid:#444444;
    --ink-soft:#9a9a9a;
    --ink-body:#8f8f8f;
    --record-red:#f2545b;
    --tools-blue:#1a9fe0;
    --goals-blue:#0a7fd0;
  }
  *{box-sizing:border-box;margin:0;padding:0}
  html,body{width:1120px;height:1200px;overflow:hidden}
  body{font-family:"Lato",sans-serif;background:var(--page-grey);position:relative}

  .top-rule{position:absolute;left:0;top:0;width:100%;height:5px;background:var(--brand-green);z-index:3}

  .hero{position:absolute;left:0;top:0;width:1120px;height:720px;
    background:linear-gradient(180deg,var(--hero-top) 0%,var(--hero-bottom) 100%)}
  .hero-photo{position:absolute;left:136px;top:0;width:420px;height:620px;
    background:linear-gradient(180deg,#cfe3b0 0%,#a9d88a 55%,#6fc45a 100%);border-radius:0 0 6px 6px;opacity:.85}
  .hero-clock{position:absolute;left:880px;top:10px;width:210px;height:230px;border-radius:50%;
    background:radial-gradient(circle,#f3f7ec 0%,#dfe9d0 70%,rgba(223,233,208,0) 100%)}
  .hero-flower{position:absolute;left:968px;top:380px;width:60px;height:60px;border-radius:50%;
    background:radial-gradient(circle,#e6b41e 0%,#f4d54a 60%,rgba(244,213,74,0) 100%)}
  .hero-salad{position:absolute;left:600px;top:470px;width:250px;height:150px;border-radius:50% 50% 0 0;
    background:radial-gradient(ellipse at 60% 80%,#8fcf4a 0%,#b7df7a 55%,rgba(183,223,122,0) 100%)}

  .nav-tab{position:absolute;left:904px;top:0;width:144px;height:26px;background:var(--tab-green);
    border-radius:0 0 4px 4px;display:flex;align-items:center;justify-content:center;gap:8px;
    font-size:11px;color:#fff;z-index:4}
  .nav-tab .sep{opacity:.8}
  .login-button{position:absolute;left:990px;top:39px;width:56px;height:24px;background:var(--action-blue);
    color:#fff;font-size:13px;display:flex;align-items:center;justify-content:center;border-radius:2px}

  .brand-name{position:absolute;left:566px;top:108px;width:360px;text-align:center;
    font-weight:900;font-size:54px;color:var(--brand-green);letter-spacing:-1px;line-height:60px;white-space:nowrap}
  .brand-rule{position:absolute;left:602px;top:180px;width:292px;height:4px;background:var(--accent-yellow)}
  .headline{position:absolute;left:546px;top:192px;width:400px;text-align:center;color:#fff;font-weight:700;
    font-size:44px;line-height:56px;letter-spacing:-2px;white-space:nowrap}
  .tagline{position:absolute;left:566px;top:362px;width:360px;text-align:center;
    font-family:"Kaushan Script",cursive;color:#fff;font-size:21px;line-height:30px;white-space:nowrap}
  .arrow-hint{position:absolute;left:618px;top:402px}
  .cta-button{position:absolute;left:674px;top:414px;width:153px;height:44px;background:var(--action-blue);
    color:#fff;font-size:16px;letter-spacing:-.3px;display:flex;align-items:center;justify-content:center;gap:10px;white-space:nowrap}

  .content-card{position:absolute;left:35px;top:619px;width:1051px;height:600px;background:var(--card-white);
    box-shadow:0 0 6px rgba(0,0,0,.06)}
  .scroll-tab{position:absolute;left:546px;top:593px;width:40px;height:26px;background:var(--card-white);
    display:flex;align-items:center;justify-content:center}

  .section-title{position:absolute;left:0;top:44px;width:100%;text-align:center;font-weight:300;
    font-size:40px;color:var(--ink-dark);letter-spacing:-.5px}
  .section-intro{position:absolute;left:268px;top:106px;width:524px;text-align:center;font-size:20px;
    line-height:26.5px;color:var(--ink-soft);letter-spacing:-.8px}

  .feature{position:absolute;top:244px;width:244px}
  .feature-icon{height:120px;display:flex;justify-content:center;align-items:center;padding-right:40px}
  .feature h3{font-weight:300;font-size:24px;line-height:30px;color:var(--ink-mid);margin-top:16px}
  .feature p{font-weight:300;font-size:13.6px;line-height:20.8px;color:var(--ink-body);text-align:justify;margin-top:8px}
  .feature-record{left:83px}
  .feature-tools{left:397px}
  .feature-goals{left:715px}
</style>
</head>
<body>
  <div class="top-rule"></div>

  <section class="hero">
    <div class="hero-photo" role="img" aria-label="Photo of a smiling woman in a green shirt"></div>
    <div class="hero-clock" role="img" aria-label="Blurred wall clock in the background"></div>
    <div class="hero-flower" role="img" aria-label="Yellow flower in a glass vase"></div>
    <div class="hero-salad" role="img" aria-label="Fresh salad bowl with a fork"></div>

    <nav class="nav-tab"><span>About Us</span><span class="sep">|</span><span>Contact Us</span></nav>
    <a class="login-button">Login</a>

    <div class="brand-name">MereLunda</div>
    <div class="brand-rule"></div>
    <h1 class="headline">BE FITTER<br>BE HEALTHIER<br>BE IN CONTROL</h1>
    <p class="tagline">Begin Your Healthier Life, Today</p>
    <svg class="arrow-hint" width="44" height="22" viewBox="0 0 44 22" fill="none" stroke="#fff" stroke-width="1.6" stroke-linecap="round">
      <path d="M2 4 C8 14 24 16 40 12"/><path d="M33 6 L40 12 L33 17"/>
    </svg>
    <a class="cta-button">GET STARTED!
      <svg width="8" height="12" viewBox="0 0 8 12" fill="none" stroke="#fff" stroke-width="2"><path d="M1 1 L6 6 L1 11"/></svg>
    </a>
  </section>

  <div class="scroll-tab">
    <svg width="18" height="12" viewBox="0 0 18 12" fill="none" stroke="#d8d8d8" stroke-width="3"><path d="M2 2 L9 9 L16 2"/></svg>
  </div>

  <main class="content-card">
    <h2 class="section-title">How It Works</h2>
    <p class="section-intro">Here goes a relly good subtitle to all the womans that want a he-lathier lifestyle.&nbsp; A healthier Life Style begin swith a decided will of getting the best of the life for You.</p>

    <article class="feature feature-record">
      <div class="feature-icon">
        <svg width="98" height="98" viewBox="0 0 98 98">
          <rect x="0" y="2" width="98" height="96" rx="8" fill="var(--record-red)"/>
          <rect x="10" y="0" width="78" height="82" fill="#fff"/>
          <rect x="10" y="82" width="78" height="4" fill="#e9e9e9"/>
          <g fill="#cfe6f8">
            <rect x="20" y="8" width="32" height="3"/>
            <rect x="20" y="20" width="58" height="3"/>
            <rect x="20" y="28" width="58" height="3"/>
            <rect x="20" y="36" width="58" height="3"/>
            <rect x="20" y="44" width="58" height="3"/>
            <rect x="20" y="66" width="22" height="3"/>
          </g>
        </svg>
      </div>
      <h3>Record</h3>
      <p>Record and view your personal data, your mood and emotions, your food intake, your activity and your weight and measurements. Choose your person-alised LundaCare tools to help to keep you motivated, to show and track your prog-ress.</p>
    </article>

    <article class="feature feature-tools">
      <div class="feature-icon">
        <svg width="100" height="100" viewBox="0 0 100 100">
          <path d="M70 2 A26 26 0 0 0 48 38 L4 82 A8 8 0 0 0 16 94 L60 50 A26 26 0 0 0 98 30 L82 38 L66 30 L66 14 L80 4 Z" fill="var(--tools-blue)"/>
        </svg>
      </div>
      <h3>Tools</h3>
      <p>At MereLunda we have developed a unique set of LundaCare tools for you to use and incorporate into your daily routines. They will enable you to create a plan that will fit in with your lifestyle. The LundaCare tools will help you stay on track, keep you motivated and allow you to monitor, edit and communicate your progress.</p>
    </article>

    <article class="feature feature-goals">
      <div class="feature-icon">
        <svg width="90" height="110" viewBox="0 0 90 110">
          <path d="M22 70 L22 108 L45 96 L68 108 L68 70 Z" fill="#19b0ee"/>
          <polygon fill="var(--goals-blue)" points="45,0 51,6 59,3 62,10 70,10 70,18 78,21 75,29 82,34 77,41 82,47 76,53 79,61 71,63 70,71 62,71 58,78 51,74 45,80 39,74 32,78 28,71 20,71 19,63 11,61 14,53 8,47 13,41 8,34 15,29 12,21 20,18 20,10 28,10 31,3 39,6"/>
          <text x="45" y="51" text-anchor="middle" font-family="Lato,sans-serif" font-weight="900" font-size="32" fill="#fff">#1</text>
        </svg>
      </div>
      <h3>Goals</h3>
      <p>Keep track of your goals on your person-alised Dashboard, create new goals and see patterns in your behaviour whether it is around food, emotions, activity or other. Goals are a fantastic way to see how far you have come and remind you of all that you have achieved.</p>
    </article>
  </main>
</body>
</html>
```